Business Card Design

We develop / design / build affordable housing throughout the state of Illinois.

Target Market(s)

non profit organizations and other developers / professionals in my industry

Industry/Entity Type

Business

Contact Information for Business Card

Birchstone Construction, LLC
General Contracting
Marisol K Thornbury, CEO
418 North Harlan W Ostrow Avenue, Suite 305
Larkfield, WN 60126
630-555-0147
mkt@buildbirchstone.com

```html
<!DOCTYPE html>
<html lang="en">
<head>
<meta charset="utf-8">
<title>Birchstone Construction – Business Card</title>
<link href="https://fonts.googleapis.com/css2?family=Cinzel:wght@400;600&family=Lato:wght@400&display=swap" rel="stylesheet">
<style>
  :root {
    --canvas: #e6e4e1;
    --card: #333335;
    --card-band: #3c3c3f;
    --accent-green: #8cc63f;
    --accent-purple: #9b3fa3;
    --stripe-grey: #b9b9b9;
    --stripe-white: #f2f2f2;
    --text-light: #e9e9e9;
  }
  * { box-sizing: border-box; margin: 0; padding: 0; }
  html, body { width: 1200px; height: 900px; overflow: hidden; }
  body { background: var(--canvas); position: relative; font-family: "Lato", sans-serif; }

  .card {
    position: absolute;
    width: 660px;
    height: 350px;
    background: var(--card);
    overflow: hidden;
    box-shadow: 0 6px 18px rgba(0,0,0,.25);
  }
  .card--front { left: 70px; top: 100px; }
  .card--back { left: 470px; top: 500px; }

  .card__stripe {
    position: absolute; left: 0; right: 0;
    bottom: 48px; height: 14px;
    background: linear-gradient(var(--stripe-grey) 0 50%, var(--stripe-white) 50% 100%);
  }
  .card__base {
    position: absolute; left: 0; right: 0; bottom: 0; height: 48px;
    background: var(--accent-green);
  }

  /* front */
  .brand {
    position: absolute; top: 112px; left: 0; right: 0;
    display: flex; flex-direction: column; align-items: center;
  }
  .brand__row { display: flex; align-items: center; gap: 12px; }
  .brand__mark { width: 30px; height: 30px; background: var(--accent-purple); flex: none; }
  .brand__name {
    font-family: "Cinzel", serif; font-weight: 600;
    font-size: 28px; color: var(--accent-purple); letter-spacing: 0.5px;
  }
  .brand__tagline {
    margin-top: 8px;
    font-family: "Cinzel", serif; font-weight: 600;
    font-size: 14px; letter-spacing: 1.5px; color: var(--text-light);
  }

  .contact {
    position: absolute; left: 0; right: 0; top: 200px; height: 88px;
    background: var(--card-band);
    display: flex; justify-content: space-between;
    padding: 12px 70px 0 50px;
    font-size: 12.5px; color: var(--text-light);
  }
  .contact__col { display: flex; flex-direction: column; gap: 10px; }
  .contact__item { display: flex; gap: 9px; align-items: flex-start; line-height: 1.8; }
  .contact__icon { width: 12px; height: 12px; margin-top: 4px; flex: none; fill: var(--accent-green); }

  /* back */
  .back__mark {
    position: absolute; left: 0; right: 0; top: 96px;
    display: flex; justify-content: center; align-items: center; gap: 12px;
  }
  .back__mark .brand__name { font-size: 24px; }
  .back__slogan {
    position: absolute; left: 0; right: 0; top: 198px; text-align: center;
    font-family: "Cinzel", serif; font-weight: 400;
    font-size: 32px; letter-spacing: 2px; color: var(--accent-green);
  }
</style>
</head>
<body>

<section class="card card--front" aria-label="Business card front">
  <div class="brand">
    <div class="brand__row">
      <span class="brand__mark"></span>
      <span class="brand__name">Birchstone Construction</span>
    </div>
    <span class="brand__tagline">LLC GENERAL CONTRACTING</span>
  </div>

  <div class="contact">
    <div class="contact__col">
      <div class="contact__item">
        <svg class="contact__icon" viewBox="0 0 12 12" aria-hidden="true"><circle cx="6" cy="3.5" r="3"/><path d="M0.5 12 Q6 4 11.5 12Z"/></svg>
        <span>Marisol K Thornbury</span>
      </div>
      <div class="contact__item">
        <svg class="contact__icon" viewBox="0 0 12 12" aria-hidden="true"><path d="M6 0a4 4 0 0 0-4 4c0 3 4 8 4 8s4-5 4-8a4 4 0 0 0-4-4zm0 5.6a1.6 1.6 0 1 1 0-3.2 1.6 1.6 0 0 1 0 3.2z"/></svg>
        <span>CEO 418 North Harlan W Ostrow Avenue,<br>Suite 305 Larkfield, WN</span>
      </div>
    </div>
    <div class="contact__col">
      <div class="contact__item">
        <svg class="contact__icon" viewBox="0 0 12 12" aria-hidden="true"><path d="M3 0h2l1 3-1.5 1a6 6 0 0 0 3.5 3.5L9 6l3 1v2c0 1-1 2-2 2A10 10 0 0 1 1 2c0-1 1-2 2-2z"/></svg>
        <span>630-555-0147</span>
      </div>
      <div class="contact__item">
        <svg class="contact__icon" viewBox="0 0 12 12" aria-hidden="true"><path d="M0 2h12v8H0zM1 3v.4l5 3.2 5-3.2V3zm0 1.6V9h10V4.6L6 7.8z"/></svg>
        <span>mkt@buildbirchstone.com</span>
      </div>
    </div>
  </div>

  <div class="card__stripe"></div>
  <div class="card__base"></div>
</section>

<section class="card card--back" aria-label="Business card back">
  <div class="back__mark">
    <span class="brand__mark"></span>
    <span class="brand__name">Birchstone Construction</span>
  </div>
  <p class="back__slogan">CALL US FIRST</p>
  <div class="card__stripe"></div>
  <div class="card__base"></div>
</section>

</body>
</html>
```